Alcohol designs Birthday Sign's needs more templates

We are after 10 new designs for signable custom birthday signs, alcohol theme inspired (beer, wine, spirits) for this batch, You do not need to provide 10 designs however the winner will be based on final look and quantity.
For example someone may win with one design or ten designs. We will also look at purchasing more individual designs for any winners or potential winners. Designs must be in layers, CMYK, 8bits channel, saved as TIFF or PDS or AI, size is 460mm wide x by 1060mm high with 30mm bleed included, total graphic size will be 430 x 1030 at 300ppi, any text must be editable and font files included. see attached for sample's, signable area needs to be on each design and a sample persons name, other then that we a excited to see what everyone comes up with
Reason: Allow more designs to be supplied form current designers and new designers. Also to allow us to choose more than one designer by adding a second/third place
Birthday
- Layers.
- Space for people to sign
- At least 3 designs (These can be of the same template you design just with a small them change beer, wine etc)

```html
<!DOCTYPE html>
<html lang="en">
<head>
<meta charset="utf-8">
<title>Birthday Sign Templates – Beer, Spirits, Wine</title>
<link rel="stylesheet" href="https://fonts.googleapis.com/css2?family=Anton&family=Oswald:wght@400;600;700&family=Great+Vibes&display=swap">
<style>
  :root {
    --backdrop: #e8e6e1;
    --sign-white: #ffffff;
    --sun-yellow: #f7c61a;
    --soft-yellow: #fbe27a;
    --wheat-gold: #e8a915;
    --ribbon-red: #b8141a;
    --headline-red: #e3151b;
    --ink-black: #1d1d1d;
    --script-brown: #7a5a2e;
  }
  html, body {
    margin: 0;
    padding: 0;
    width: 1058px;
    height: 1200px;
    overflow: hidden;
    background: var(--backdrop);
  }
  .sign-row {
    position: absolute;
    left: 34px;
    top: 228px;
    display: flex;
    gap: 30px;
  }
  .birthday-sign {
    width: 310px;
    height: 743px;
    display: block;
    background: var(--sign-white);
    box-shadow: 0 4px 14px rgba(0,0,0,0.18);
  }
  .headline-small { font-family: "Oswald", sans-serif; font-weight: 700; fill: var(--ink-black); }
  .headline-drink { font-family: "Anton", sans-serif; }
  .headline-drink.beer { fill: var(--sun-yellow); stroke: var(--headline-red); stroke-width: 2.5px; paint-order: stroke; }
  .headline-drink.wine { fill: var(--headline-red); }
  .headline-family { font-family: "Oswald", sans-serif; font-weight: 700; fill: var(--headline-red); }
  .ribbon-area { fill: var(--ribbon-red); }
  .ribbon-date { font-family: "Oswald", sans-serif; font-weight: 400; fill: #fff; }
  .greeting-script { font-family: "Great Vibes", cursive; fill: var(--script-brown); }
  .celebrant-name { font-family: "Oswald", sans-serif; font-weight: 700; }
  .celebrant-name.beer { fill: var(--headline-red); }
  .celebrant-name.wine { fill: var(--script-brown); }
  .wheat-strip { fill: var(--wheat-gold); }
</style>
</head>
<body>
<div class="sign-row">

  <!-- Beer sign -->
  <svg class="birthday-sign" viewBox="0 0 310 743" xmlns="http://www.w3.org/2000/svg">
    <defs>
      <linearGradient id="beerSignSpace" x1="0" y1="0" x2="0" y2="1">
        <stop offset="0" stop-color="#f4f4f4"/>
        <stop offset="1" stop-color="#ffffff"/>
      </linearGradient>
      <linearGradient id="beerMugsTone" x1="0" y1="0" x2="0" y2="1">
        <stop offset="0" stop-color="#f5f1e6"/>
        <stop offset="0.25" stop-color="#e6a21c"/>
        <stop offset="1" stop-color="#b8680c"/>
      </linearGradient>
    </defs>
    <rect class="sign-frame" x="0" y="0" width="310" height="743" fill="var(--sun-yellow)"/>
    <rect class="sign-inner" x="10" y="10" width="290" height="723" fill="url(#beerSignSpace)"/>
    <path class="top-splash" d="M10 120 H300 V300 Q260 280 220 300 Q160 270 110 290 Q60 275 10 300 Z" fill="var(--soft-yellow)"/>
    <rect role="img" aria-label="Two frothy beer mugs clinking" x="40" y="22" width="230" height="220" rx="18" fill="url(#beerMugsTone)"/>

    <text class="headline-small" transform="translate(50 318) rotate(-90)" font-size="22" textLength="58" lengthAdjust="spacingAndGlyphs">HAPPY</text>
    <text class="headline-drink beer" x="56" y="318" font-size="68" textLength="140" lengthAdjust="spacingAndGlyphs">BEER</text>
    <text class="headline-small" transform="translate(234 318) rotate(-90)" font-size="30" textLength="58" lengthAdjust="spacingAndGlyphs">FUN</text>
    <text class="headline-family" transform="translate(272 370) rotate(-90)" font-size="32" textLength="108" lengthAdjust="spacingAndGlyphs">FAMILY</text>
    <text class="headline-small" x="26" y="368" font-size="48" textLength="210" lengthAdjust="spacingAndGlyphs">GOOD TIMES</text>

    <g class="date-ribbon" transform="rotate(4 155 412)">
      <rect class="ribbon-area" role="img" aria-label="Red ribbon banner" x="22" y="390" width="266" height="44" rx="4"/>
      <text class="ribbon-date" x="155" y="421" font-size="25" text-anchor="middle">26.06.1993</text>
    </g>

    <path class="bottom-splash" d="M10 650 Q60 615 120 632 Q180 605 240 628 Q280 615 300 632 V733 H10 Z" fill="var(--sun-yellow)" opacity="0.75"/>
    <text class="greeting-script" x="155" y="680" font-size="30" text-anchor="middle">Happy Birthday</text>
    <text class="celebrant-name beer" x="155" y="708" font-size="24" text-anchor="middle">MARLO</text>
    <rect class="wheat-strip" role="img" aria-label="Row of wheat ear ornaments" x="20" y="717" width="270" height="10" rx="5"/>
  </svg>

  <!-- Spirits sign -->
  <svg class="birthday-sign" viewBox="0 0 310 743" xmlns="http://www.w3.org/2000/svg">
    <defs>
      <linearGradient id="spiritsBackdrop" x1="0" y1="0" x2="0" y2="1">
        <stop offset="0" stop-color="#f9cf2c"/>
        <stop offset="0.42" stop-color="#fbdf73"/>
        <stop offset="0.62" stop-color="#ffffff"/>
      </linearGradient>
      <linearGradient id="spiritsGlassesTone" x1="0" y1="0" x2="1" y2="0">
        <stop offset="0" stop-color="#e46a2a"/>
        <stop offset="0.5" stop-color="#d9e6ea"/>
        <stop offset="1" stop-color="#d79a22"/>
      </linearGradient>
    </defs>
    <rect x="0" y="0" width="310" height="743" fill="url(#spiritsBackdrop)"/>
    <path class="top-splash" d="M0 60 Q60 40 120 55 Q200 30 310 70 V230 Q240 250 170 235 Q90 255 0 230 Z" fill="#ffffff" opacity="0.9"/>
    <rect role="img" aria-label="Three cocktail glasses with splashing spirits and ice" x="75" y="30" width="160" height="215" rx="14" fill="url(#spiritsGlassesTone)"/>

    <text class="headline-small" transform="translate(50 338) rotate(-90)" font-size="22" textLength="58" lengthAdjust="spacingAndGlyphs">HAPPY</text>
    <text class="headline-drink wine" x="56" y="338" font-size="68" textLength="140" lengthAdjust="spacingAndGlyphs">WINE</text>
    <text class="headline-small" transform="translate(234 338) rotate(-90)" font-size="30" textLength="58" lengthAdjust="spacingAndGlyphs">FUN</text>
    <text class="headline-family" transform="translate(272 390) rotate(-90)" font-size="32" textLength="108" lengthAdjust="spacingAndGlyphs">FAMILY</text>
    <text class="headline-small" x="26" y="388" font-size="48" textLength="210" lengthAdjust="spacingAndGlyphs">GOOD TIMES</text>

    <g class="date-ribbon" transform="rotate(4 155 432)">
      <rect class="ribbon-area" role="img" aria-label="Red ribbon banner" x="22" y="410" width="266" height="44" rx="4"/>
      <text class="ribbon-date" x="155" y="441" font-size="25" text-anchor="middle">26.06.1993</text>
    </g>

    <text class="greeting-script" x="155" y="690" font-size="30" text-anchor="middle">Happy Birthday</text>
    <text class="celebrant-name wine" x="155" y="722" font-size="24" text-anchor="middle">MARLO</text>
  </svg>

  <!-- Wine sign -->
  <svg class="birthday-sign" viewBox="0 0 310 743" xmlns="http://www.w3.org/2000/svg">
    <defs>
      <linearGradient id="wineBackdrop" x1="0" y1="0" x2="0" y2="1">
        <stop offset="0" stop-color="#f9cf2c"/>
        <stop offset="0.42" stop-color="#fbdf73"/>
        <stop offset="0.62" stop-color="#ffffff"/>
      </linearGradient>
      <linearGradient id="wineGlassesTone" x1="0" y1="0" x2="1" y2="0">
        <stop offset="0" stop-color="#9e1a2c"/>
        <stop offset="0.55" stop-color="#e7c2c8"/>
        <stop offset="1" stop-color="#f1e6d6"/>
      </linearGradient>
    </defs>
    <rect x="0" y="0" width="310" height="743" fill="url(#wineBackdrop)"/>
    <path class="top-splash" d="M0 60 Q60 40 120 55 Q200 30 310 70 V230 Q240 250 170 235 Q90 255 0 230 Z" fill="#ffffff" opacity="0.9"/>
    <rect role="img" aria-label="Red and white wine glasses clinking with a splash" x="80" y="45" width="170" height="200" rx="14" fill="url(#wineGlassesTone)"/>

    <text class="headline-small" transform="translate(50 338) rotate(-90)" font-size="22" textLength="58" lengthAdjust="spacingAndGlyphs">HAPPY</text>
    <text class="headline-drink wine" x="56" y="338" font-size="68" textLength="140" lengthAdjust="spacingAndGlyphs">WINE</text>
    <text class="headline-small" transform="translate(234 338) rotate(-90)" font-size="30" textLength="58" lengthAdjust="spacingAndGlyphs">FUN</text>
    <text class="headline-family" transform="translate(272 390) rotate(-90)" font-size="32" textLength="108" lengthAdjust="spacingAndGlyphs">FAMILY</text>
    <text class="headline-small" x="26" y="388" font-size="48" textLength="210" lengthAdjust="spacingAndGlyphs">GOOD TIMES</text>

    <g class="date-ribbon" transform="rotate(4 155 432)">
      <rect class="ribbon-area" role="img" aria-label="Red ribbon banner" x="22" y="410" width="266" height="44" rx="4"/>
      <text class="ribbon-date" x="155" y="441" font-size="25" text-anchor="middle">26.06.1993</text>
    </g>

    <text class="greeting-script" x="155" y="690" font-size="30" text-anchor="middle">Happy Birthday</text>
    <text class="celebrant-name wine" x="155" y="722" font-size="24" text-anchor="middle">MARLO</text>
  </svg>

</div>
</body>
</html>
```